"1" Pager Webdesign + HTML Creation

In this project we ask you to create a 1 pager (the registration form will be opened on a second page) web design with the content & structure described in the attached PDF. You are absolutely free in your choice of colors & design. There is also no company logo on this site as it will serve as a demo site for future clients where the design & content can be adjusted.
Once we agree on the design we also ask you to convert it into a simple html page.
The site is not a regular company website with services etc. --> the main idea is to give client the ability to launch a dedicated server (VPS) fully automatically in the background from the web gui. This server will have a software installed that allows phishing simulations to test employees security awareness.....so there should be some logical flow from top to bottom that leads to the user to launch the server. The company details/ressources etc. are not important and can be really kept very small. Main point of the site is to explain user what the steps he needs to go through to launch that virtual server...so launch button must be also kinda big...
See example I created (jpg) --> I am not designer. This is just to illustrate what I mean with logical "flow"....
As for pricing: I don't expect a fully functional html site & finished design for this price and I am willing to pay an extra bonus for finalizing the design/site as I know the details are time consuming. This bonus could be agreed upon project start and paid via coinwell. What I want are a few design examples that show that you understood what I need. Depending how much custom graphics need to be created we can discuss extra bonus/time required...
The site is not a regular company website with services etc. --> the main idea is to give client the ability to launch a dedicated server (VPS) fully automatically in the background from the web gui. This server will have a software installed that allows phishing simulations to test employees security awareness.....so there should be some logical flow from top to bottom that leads to the user to launch the server.... Added Thursday, August 11, 2016
Coding
Coded - Design and coding required
Number of Pages Required
2 page

```html
<!DOCTYPE html>
<html lang="en">
<head>
<meta charset="utf-8">
<title>Baitline GmbH – Human Phishing &amp; Malware Defense</title>
<link href="https://fonts.googleapis.com/css2?family=Open+Sans:wght@400;600;700&family=Roboto:wght@400;500;700;900&display=swap" rel="stylesheet">
<style>
:root{
  --blue:#2a9ad9;
  --blue-deep:#1f7fc0;
  --blue-dark:#14507f;
  --orange:#fbb117;
  --ink:#333;
  --muted:#555;
  --white:#fff;
  --grey-bg:#f1f1f1;
  --dark:#3b3b3b;
  --darker:#262626;
}
*{box-sizing:border-box;margin:0;padding:0}
html,body{width:1200px;height:4911px;overflow:hidden}
body{font-family:"Open Sans",Arial,sans-serif;color:var(--ink);background:var(--white);position:relative}
section,header,footer{position:absolute;left:0;width:1200px}
.abs{position:absolute}
.brand{font-family:"Roboto",Arial,sans-serif;font-weight:500;letter-spacing:1px}

/* header */
.site-header{top:0;height:63px;background:var(--white);box-shadow:0 1px 3px rgba(0,0,0,.08);z-index:2}
.site-header .brand{left:130px;top:16px;font-size:26px;color:var(--blue)}
.nav{position:absolute;top:0;left:598px;height:63px;display:flex;align-items:center;gap:0}
.nav a{font-family:"Roboto",sans-serif;font-size:11.5px;color:#444;text-decoration:none;padding:9px 15px;font-weight:500}
.nav a.active{background:var(--orange);color:var(--white);margin-right:15px}

/* hero */
.hero{top:63px;height:588px;background:linear-gradient(135deg,#3d9fe0 0%,#2b8fd6 45%,#4aa8e6 100%)}
.hero-photo{position:absolute;inset:0;background:radial-gradient(ellipse at 30% 30%,rgba(255,255,255,.18),transparent 55%),radial-gradient(ellipse at 80% 70%,rgba(255,255,255,.12),transparent 50%)}
.hero h1{position:absolute;top:42px;width:100%;text-align:center;font-family:"Roboto",sans-serif;font-weight:900;font-size:38px;color:var(--white)}
.hero p.lead{position:absolute;top:92px;left:300px;width:600px;text-align:center;font-size:15px;line-height:21px;color:var(--white)}
.btn{position:absolute;display:flex;align-items:center;justify-content:center;font-family:"Roboto",sans-serif;font-weight:700;text-decoration:none;color:var(--white)}
.btn-watch{left:433px;top:158px;width:160px;height:40px;background:var(--orange);font-size:14px}
.btn-learn{left:603px;top:158px;width:162px;height:40px;background:var(--blue-dark);font-size:14px}
.laptop{left:262px;top:223px}

/* intro */
.intro{top:651px;height:513px;background:var(--white)}
.tag{left:536px;top:68px;width:128px;height:31px;border:1px solid #bbb;display:flex;align-items:center;justify-content:center;font-size:13px;color:#333}
.intro h2{position:absolute;top:115px;width:100%;text-align:center;font-family:"Roboto",sans-serif;font-weight:700;font-size:23px;color:var(--blue)}
.intro .with{position:absolute;top:151px;width:100%;text-align:center;font-size:13px;color:#444}
.ring{position:absolute;border:2px solid var(--blue);border-radius:50%;display:flex;align-items:center;justify-content:center}
.intro .ring{width:130px;height:130px}
.feat-title{position:absolute;font-family:"Roboto",sans-serif;font-weight:700;font-size:13.5px;color:#222;text-align:center}
.feat-text{position:absolute;font-size:12px;line-height:20px;color:#444;text-align:center}

/* how it works */
.how{top:1164px;height:1416px;background:linear-gradient(160deg,#2b98dc 0%,#2690d6 50%,#2f9de0 100%)}
.how h2{position:absolute;top:38px;width:100%;text-align:center;font-family:"Roboto",sans-serif;font-weight:700;font-size:23px;color:var(--white)}
.how .sub{position:absolute;top:76px;width:100%;text-align:center;font-size:12px;color:var(--white)}
.how .disc{position:absolute;width:112px;height:112px;border-radius:50%;background:var(--white);display:flex;align-items:center;justify-content:center}
.col-text{position:absolute;top:278px;width:260px;font-size:11.5px;line-height:19.5px;color:var(--white)}
.col-text b{display:block;font-weight:700}
.col-text .spacer{height:10px}
.vline{position:absolute;top:130px;width:1px;height:299px;background:rgba(255,255,255,.45)}
.hline{position:absolute;left:132px;top:473px;width:936px;height:1px;background:rgba(255,255,255,.45)}
.steps{position:absolute;left:0;top:0}
.step{position:absolute;font-size:12px;line-height:20px;color:var(--white)}
.step h3{font-family:"Roboto",sans-serif;font-size:13px;font-weight:700;margin-bottom:8px;color:var(--white)}
.step h3 span{color:var(--orange)}
.step.right{text-align:right}

/* get started */
.start{top:2580px;height:593px;background:var(--white)}
.start h2{position:absolute;top:48px;width:100%;text-align:center;font-family:"Roboto",sans-serif;font-weight:700;font-size:23px;color:var(--blue)}
.start .sub{position:absolute;top:94px;left:170px;width:860px;text-align:center;font-size:12px;line-height:20px;color:#444}
.video{position:absolute;overflow:hidden}
.video .frame{position:absolute;left:0;top:0;right:0}
.play{position:absolute;border-radius:50%;background:#d9262b;display:flex;align-items:center;justify-content:center}
.controls{position:absolute;left:0;right:0;bottom:0;background:#1b1b1b;display:flex;align-items:center;color:#ddd;font-size:10px;padding:0 10px;gap:14px}
.controls .speed{margin-left:auto}
.launch{position:absolute;left:716px;top:162px;width:354px;height:381px;background:var(--blue)}
.launch p{position:absolute;left:55px;top:82px;font-family:"Roboto",sans-serif;font-size:19px;line-height:30px;color:var(--white)}
.launch p em{font-style:normal;color:var(--orange);font-weight:500}
.badge{position:absolute;left:57px;top:231px;width:149px;height:38px;background:#eee;border:2px solid #999}

/* resources */
.res{top:3173px;height:630px;background:var(--grey-bg)}
.res h2{position:absolute;top:34px;width:100%;text-align:center;font-family:"Roboto",sans-serif;font-weight:700;font-size:23px;color:var(--blue)}
.res .divider{position:absolute;left:599px;top:75px;width:1px;height:206px;background:#d6d6d6}
.res-col{position:absolute;top:100px;width:420px;text-align:center}
.res-col h3{margin-top:16px;font-family:"Roboto",sans-serif;font-size:14px;font-weight:700;color:#222}
.res-col p{margin-top:10px;font-size:12px;line-height:20px;color:#444}
.btn-dl{position:absolute;top:279px;width:152px;height:32px;background:var(--orange);font-size:14px}

/* about */
.about{top:3803px;height:654px;background:linear-gradient(160deg,#474747 0%,#3a3a3a 60%,#333 100%)}
.about h2{position:absolute;left:132px;top:36px;font-family:"Roboto",sans-serif;font-weight:700;font-size:23px;color:var(--blue)}
.about .story{position:absolute;left:132px;top:80px;width:602px;font-size:11.5px;line-height:20px;color:#cfcfcf}
.about .brand{position:absolute;left:786px;top:132px;font-size:34px;color:var(--blue)}
.about h4{position:absolute;font-family:"Roboto",sans-serif;font-weight:700;font-size:14px;color:var(--white)}
.pin{position:absolute;left:130px;top:4043px}
.addr{position:absolute;left:181px;top:240px;font-size:11.5px;line-height:21px;color:var(--white)}
.follow{position:absolute;left:132px;top:313px;display:flex;align-items:center;gap:5px;font-family:"Roboto",sans-serif;font-size:10px;font-weight:700;color:var(--white)}
.follow .sq{width:17px;height:17px;border-radius:2px}
.follow .label{margin-right:8px}
.map{position:absolute;left:132px;top:356px;width:492px;height:248px;background:linear-gradient(135deg,#e9e4d8,#dcd6c6);border:1px solid #999}
.form{position:absolute;left:677px;top:267px;width:391px}
.field{position:absolute;left:0;width:391px;background:var(--white);font-size:12px;color:#444;padding:0 16px;display:flex;align-items:center}
.field.area{align-items:flex-start;padding-top:14px}
.submit{position:absolute;left:0;top:277px;width:391px;height:59px;background:var(--orange);color:var(--darker);font-family:"Roboto",sans-serif;font-weight:700;font-size:19px;display:flex;align-items:center;justify-content:center}

/* register */
.register{top:4457px;height:372px;background:linear-gradient(180deg,#2d2d2d 0%,#3c3c3c 55%,#2a2a2a 100%)}
.register h2{position:absolute;top:110px;width:100%;text-align:center;font-family:"Roboto",sans-serif;font-weight:900;font-size:36px;color:var(--blue)}
.register p{position:absolute;top:156px;width:100%;text-align:center;font-size:15px;color:var(--white)}
.btn-register{left:456px;top:200px;width:286px;height:67px;background:var(--orange);color:#3a3a3a;font-size:24px;font-weight:900}

/* footer */
.site-footer{top:4829px;height:82px;background:var(--blue)}
.site-footer .brand{position:absolute;left:130px;top:24px;font-size:27px;color:var(--white)}
.site-footer .copy{position:absolute;right:132px;top:35px;font-size:11.5px;color:var(--white)}
</style>
</head>
<body>

<header class="site-header">
  <div class="brand abs">Baitline GmbH</div>
  <nav class="nav">
    <a class="active" href="#top">TOP</a>
    <a href="#intro">INTRO</a>
    <a href="#how">HOW IT WORKS</a>
    <a href="#resources">RESSOURCES</a>
    <a href="#about">ABOUT US</a>
  </nav>
</header>

<section class="hero" id="top">
  <div class="hero-photo" role="img" aria-label="Blue-toned photo of an office team working together"></div>
  <h1>START TO PHISH!</h1>
  <p class="lead">Raising your Security Posture means securing the people. Isn't it time that we invest in our people as seriously as we invest in technology?</p>
  <a class="btn btn-watch" href="#video">WATCH VIDEO</a>
  <a class="btn btn-learn" href="#how">LEARN MORE</a>
  <svg class="abs laptop" width="676" height="395" viewBox="0 0 676 395">
    <rect x="66" y="0" width="546" height="368" rx="14" fill="#1e1e1e"/>
    <rect x="82" y="22" width="514" height="324" fill="#5d7586"/>
    <rect x="0" y="368" width="676" height="14" rx="3" fill="#d8d8d8"/>
    <path d="M0 382 H676 Q660 395 620 395 H56 Q16 395 0 382Z" fill="#a9a9a9"/>
    <rect x="300" y="368" width="76" height="7" rx="3" fill="#bcbcbc"/>
  </svg>
  <div class="abs" role="img" aria-label="Video still of office binders labelled new employees" style="left:344px;top:245px;width:514px;height:324px;background:linear-gradient(135deg,#8aa3b4,#41596b)"></div>
  <div class="play" style="left:556px;top:372px;width:84px;height:84px">
    <svg width="34" height="38" viewBox="0 0 34 38"><path d="M4 2 L32 19 L4 36Z" fill="#fff"/></svg>
  </div>
</section>

<section class="intro" id="intro">
  <div class="tag abs">Build Your Best</div>
  <h2>HUMAN PHISHING AND MALWARE DEFENSE</h2>
  <div class="with">with us</div>
  <div class="ring" style="left:271px;top:225px">
    <svg width="50" height="54" viewBox="0 0 50 54" fill="none" stroke="#2a9ad9" stroke-width="2.5"><circle cx="25" cy="15" r="12"/><path d="M3 52 V44 Q3 34 14 34 H36 Q47 34 47 44 V52Z"/></svg>
  </div>
  <div class="ring" style="left:778px;top:225px">
    <svg width="54" height="60" viewBox="0 0 54 60" fill="none" stroke="#2a9ad9" stroke-width="2.5"><path d="M19 44 V38 Q11 33 11 24 A16 16 0 0 1 43 24 Q43 33 35 38 V44Z"/><path d="M20 49 H34 M22 54 H32"/><path d="M24 38 V28 L27 31 L30 28 V38"/><path d="M27 2 V0 M6 10 L4 8 M48 10 L50 8 M1 26 H-1 M53 26 H55"/></svg>
  </div>
  <svg class="abs" style="left:515px;top:220px" width="165" height="166" viewBox="0 0 165 166" fill="none" stroke="#999" stroke-width="1.5">
    <path d="M10 40 Q80 -10 155 28"/><path d="M145 18 L157 29 L142 33"/>
    <path d="M155 126 Q85 176 10 138"/><path d="M20 148 L8 137 L23 133"/>
  </svg>
  <div class="feat-title" style="left:186px;top:388px;width:300px">TEST YOUR USERS</div>
  <div class="feat-text" style="left:186px;top:412px;width:300px">Fully automated Spear Phishing, Malware,<br>Smihsing, &amp; USB attack Simulations</div>
  <div class="feat-title" style="left:693px;top:388px;width:300px">TRAIN YOUR USERS</div>
  <div class="feat-text" style="left:693px;top:412px;width:300px">Choose among many ondemand interactive,<br>engaging training modules (customizable tips,<br>video's, games, quiz etc.)</div>
</section>

<section class="how" id="how">
  <h2>HOW DOES IT WORK?</h2>
  <div class="sub">It's so easy. After registration you can launch a virtualized server with a full scale testing and education platform within minutes.</div>

  <div class="disc" style="left:129px;top:135px">
    <svg width="64" height="64" viewBox="0 0 64 64" fill="none" stroke="#2a9ad9" stroke-width="2.5"><path d="M28 4 H36 L38 12 L44 15 L51 10 L56 16 L51 23 L53 29 L60 30 V38 L53 39 L51 45 L55 52 L49 57 L43 52 L37 55 L36 62 H28 L27 55 L21 52 L14 57 L8 51 L13 45 L11 39 L4 38 V30 L11 28 L13 22 L8 15 L14 9 L21 14 L27 12Z"/><circle cx="32" cy="34" r="10"/></svg>
  </div>
  <div class="disc" style="left:463px;top:135px">
    <svg width="40" height="80" viewBox="0 0 40 80" fill="none" stroke="#2a9ad9" stroke-width="5"><circle cx="20" cy="18" r="14"/><circle cx="20" cy="18" r="4" fill="#2a9ad9"/><path d="M20 32 V74 H30 M20 56 H30"/></svg>
  </div>
  <div class="disc" style="left:826px;top:135px">
    <svg width="76" height="76" viewBox="0 0 76 76" fill="none" stroke="#2a9ad9" stroke-width="2.5"><circle cx="38" cy="38" r="34"/><ellipse cx="38" cy="38" rx="14" ry="34"/><path d="M6 28 H70 M6 48 H70"/><path d="M14 14 Q38 30 62 14 M14 62 Q38 46 62 62"/></svg>
  </div>

  <div class="col-text" style="left:132px"><b>BASIC SETTINGS:</b><b>Choose your preferred campaign settings</b><div class="spacer"></div>Duration of campaign (up to 3 years)<br>Number of employees to test/train<br>Technical Details (domain names etc.)<br>Choose additional services (Campaign<br>Setup Support etc.)</div>
  <div class="vline" style="left:414px"></div>
  <div class="col-text" style="left:469px"><b>ACCESS</b><b>Access your training platform</b><div class="spacer"></div>We will automatically launch a virtualized server<br>and send you the login credentials* via mail.</div>
  <div class="vline" style="left:780px"></div>
  <div class="col-text" style="left:826px"><b>WEB WIZARD</b><b>Configure your training &amp; phishing campaign</b><div class="spacer"></div>Use our simple, intuitive web based configuration<br>wizard to finish your campaign.</div>
  <div class="hline"></div>

  <svg class="steps" width="1200" height="1416" viewBox="0 0 1200 1416" fill="none" stroke="#fff" stroke-width="2">
    <path d="M277 630 V673 H933 V710"/>
    <path d="M933 815 V855 H277 V893"/>
    <path d="M277 998 V1038 H933 V1075"/>
    <path d="M933 1180 V1221 H277 V1260"/>
    <circle cx="273" cy="578" r="52"/>
    <circle cx="933" cy="763" r="52"/>
    <circle cx="273" cy="946" r="52"/>
    <circle cx="933" cy="1128" r="52"/>
    <circle cx="273" cy="1313" r="52"/>
    <!-- step icons -->
    <path d="M248 556 H254 M262 556 H268 M276 556 H282 M248 556 V562 M248 570 V576 M248 584 V590 M248 598 H254" stroke-width="3"/>
    <path d="M275 577 L298 588 L288 591 L296 603 L291 606 L283 594 L276 601Z" fill="#fff"/>
    <circle cx="933" cy="766" r="25"/><circle cx="933" cy="766" r="15"/><circle cx="933" cy="766" r="5" fill="#fff"/>
    <path d="M933 766 L958 741 M952 738 H962 V748" stroke-width="3"/>
    <path d="M248 933 V972 H298 V933 M248 933 L273 914 L298 933 M248 972 L273 950 L298 972 M255 924 V938 L273 952 L291 938 V924 Z"/>
    <rect x="905" y="1104" width="56" height="46" rx="3"/><path d="M905 1116 H961"/>
    <rect x="913" y="1124" width="10" height="18" fill="#fff"/><rect x="928" y="1124" width="10" height="18" fill="#fff"/><rect x="943" y="1124" width="10" height="18" fill="#fff"/>
    <path d="M258 1290 L297 1313 L258 1336Z" stroke-width="3"/>
  </svg>

  <div class="step" style="left:378px;top:536px;width:450px"><h3><span>STEP 1 :</span> CAMPAIGN SELECTION</h3>Select your campaign type (e.g. training only, training combined with phishing simulation etc.): Choose among a huge selection of phishing &amp; Training templates to create your basic configuration</div>
  <div class="step right" style="left:376px;top:744px;width:448px"><h3><span>STEP 2:</span> DEFINE THE TARGET</h3>Import your mail addresses (orphone numbers)</div>
  <div class="step" style="left:378px;top:918px;width:450px"><h3><span>STEP &nbsp;3 :</span> CHOOSE MAIL TEMPLATE</h3>Choose a Message template and customize the content or design tailored to your needs</div>
  <div class="step right" style="left:376px;top:1101px;width:448px"><h3><span>STEP 4:</span> CHOOSE WEB LANDING PAGE</h3>With more than 100 existing phishing &amp; malware templates you can pick a real live phishing or malware scenario that matches your company's risk profile</div>
  <div class="step" style="left:378px;top:1292px;width:450px"><h3><span>STEP &nbsp;5 :</span> START!START!</h3>Start! Start your campaign &amp; monitor the results in real time</div>
</section>

<section class="start" id="video">
  <h2>GET STARTED</h2>
  <p class="sub">Please register here and start your awareness program right away. If you are not sure which campaign fits your needs the best, please select "custom campaign" within the registration form and we will get back to you shortly to arrange a personal consultation.</p>
  <div class="video" style="left:130px;top:162px;width:586px;height:381px">
    <div class="frame" role="img" aria-label="Video still of a laptop showing a security shield on a busy desk" style="height:349px;background:linear-gradient(135deg,#6c6a62,#2f2e2b)"></div>
    <div class="play" style="left:252px;top:132px;width:84px;height:84px"><svg width="34" height="38" viewBox="0 0 34 38"><path d="M4 2 L32 19 L4 36Z" fill="#fff"/></svg></div>
    <div class="controls" style="height:32px"><span>▶</span><span>0:00 / 0:46</span><span class="speed">SPEED 1.0x</span><span>◀)</span><span>▭</span></div>
  </div>
  <div class="launch">
    <p>Launch your virtualized<br><em>Security Awareness Training</em><br>and Phishing/Malware<br>Simulation Platform</p>
    <div class="badge"></div>
  </div>
</section>

<section class="res" id="resources">
  <h2>RESSOURCES</h2>
  <div class="divider"></div>
  <div class="res-col" style="left:135px">
    <svg width="56" height="56" viewBox="0 0 64 64" fill="none" stroke="#2a9ad9" stroke-width="2.5"><path d="M28 4 H36 L38 12 L44 15 L51 10 L56 16 L51 23 L53 29 L60 30 V38 L53 39 L51 45 L55 52 L49 57 L43 52 L37 55 L36 62 H28 L27 55 L21 52 L14 57 L8 51 L13 45 L11 39 L4 38 V30 L11 28 L13 22 L8 15 L14 9 L21 14 L27 12Z"/><circle cx="32" cy="34" r="10"/></svg>
    <h3>SERVICES</h3>
    <p>There are many variations of passages of Lorem Ipsum<br>available, but the majority have suffered alteration in some form,<br>by injected humour, or randomised words</p>
  </div>
  <div class="res-col" style="left:622px">
    <svg width="52" height="56" viewBox="0 0 50 54" fill="none" stroke="#2a9ad9" stroke-width="2.5"><circle cx="25" cy="15" r="12"/><path d="M3 52 V44 Q3 34 14 34 H36 Q47 34 47 44 V52Z"/></svg>
    <h3>ABOUT US</h3>
    <p>There are many variations of passages of Lorem Ipsum<br>available, but the majority have suffered alteration in some form,<br>by injected humour, or randomised words</p>
  </div>
  <a class="btn btn-dl" href="#" style="left:277px">⤓&nbsp; DOWNLOAD</a>
  <a class="btn btn-dl" href="#" style="left:763px">⤓&nbsp; DOWNLOAD</a>
  <div class="video" style="left:130px;top:330px;width:450px;height:252px">
    <div class="frame" role="img" aria-label="Video still of a monitor in a server room" style="height:226px;background:linear-gradient(135deg,#3a6fb0,#0f2a55)"></div>
    <div class="play" style="left:196px;top:84px;width:60px;height:60px"><svg width="24" height="28" viewBox="0 0 34 38"><path d="M4 2 L32 19 L4 36Z" fill="#fff"/></svg></div>
    <div class="controls" style="height:26px;font-size:8px"><span>▶</span><span>0:00 / 0:46</span><span class="speed">SPEED 1.0x</span><span>◀)</span><span>▭</span></div>
  </div>
  <div class="video" style="left:618px;top:330px;width:448px;height:252px">
    <div class="frame" role="img" aria-label="Video still of a person working at a computer in a dim office" style="height:226px;background:linear-gradient(135deg,#4c89c2,#12243c)"></div>
    <div class="play" style="left:194px;top:84px;width:60px;height:60px"><svg width="24" height="28" viewBox="0 0 34 38"><path d="M4 2 L32 19 L4 36Z" fill="#fff"/></svg></div>
    <div class="controls" style="height:26px;font-size:8px"><span>▶</span><span>0:00 / 0:46</span><span class="speed">SPEED 1.0x</span><span>◀)</span><span>▭</span></div>
  </div>
</section>

<section class="about" id="about">
  <h2>ABOUT US</h2>
  <p class="story">We launched this service because we saw a real opportunity in leveraging the everyday employee in the fight against phishing. After all, it's the employee being targeted. Our Security Education Platform includes integrated knowledge assessments, a library of simulated attacks, and interactive training modules, which have been proven to reduce successful phishing attacks and malware infections by up to 90%. Together with our partner Lurekit we ensure that we always keep up with latest attack trends.</p>
  <div class="brand">Baitline GmbH</div>
  <h4 style="left:134px;top:202px">ADDRESS</h4>
  <svg class="abs" style="left:128px;top:240px" width="36" height="36" viewBox="0 0 36 36"><circle cx="18" cy="18" r="18" fill="#fff"/><path d="M18 8 A7 7 0 0 1 25 15 Q25 20 18 28 Q11 20 11 15 A7 7 0 0 1 18 8Z" fill="#3b3b3b"/><circle cx="18" cy="15" r="2.5" fill="#fff"/></svg>
  <div class="addr">48 Harbor Crest Road, Milbrook, CA 90210<br>T : 1.555.0142.300 &nbsp;|&nbsp; E : hello@baitline.example</div>
  <div class="follow"><span class="label">FOLLOW US ON</span><span class="sq" style="background:#3b5998"></span><span class="sq" style="background:#2aa9e0"></span><span class="sq" style="background:#dd4b39"></span><span class="sq" style="background:#0e76a8"></span></div>
  <div class="map" role="img" aria-label="Street map showing the office location"></div>
  <h4 style="left:675px;top:234px">QUESTION?</h4>
  <div class="form">
    <div class="field" style="top:0;height:46px">Name</div>
    <div class="field" style="top:53px;height:44px">E mail</div>
    <div class="field" style="top:107px;height:45px;justify-content:space-between">Select Category
      <svg width="16" height="10" viewBox="0 0 16 10" fill="none" stroke="#333" stroke-width="2"><path d="M1 1 L8 8 L15 1"/></svg></div>
    <div class="field area" style="top:162px;height:103px">Details</div>
    <div class="submit">SUBMIT</div>
  </div>
</section>

<section class="register" id="register">
  <div class="abs" role="img" aria-label="Dark photo of a hand on a laptop keyboard" style="inset:0;background:radial-gradient(ellipse at 50% 40%,rgba(255,255,255,.08),transparent 60%)"></div>
  <h2>REGISTER</h2>
  <p>The user can then enter a few selection criteria</p>
  <a class="btn btn-register" href="#register">REGISTER NOW!</a>
</section>

<footer class="site-footer">
  <div class="brand">Baitline GmbH</div>
  <div class="copy">Copyrights @ 2016 All Rights Reserved</div>
</footer>

</body>
</html>
```